I need a business card for myself, being a proprietor of a funeral parlor based in Manila. I'd like the card to have either of the following:
White Font on Black Background
or
Black Font on White Background
No logo is needed however I will appreciate any efforts to show a symbol of eternal happiness, aptly designed with above mentioned colors in mind.
Company name, address and contact on the lower right corner.
Logo or symbol anywhere.
Quillstone Funeral Services
+639174826351
darvik4521@pelmora.com
corner of Brisco Avenue and Velhurst Street
Makati City, Philippines
Thank you.
Update: Please include a small dove in your design. You are free to choose where you would like it on the card.

```html
<!DOCTYPE html>
<html lang="en">
<head>
<meta charset="utf-8">
<title>Quillstone Funeral Services – Business Card</title>
<link rel="stylesheet" href="https://fonts.googleapis.com/css2?family=Tinos:wght@700&family=Open+Sans:wght@400&display=swap">
<style>
  :root {
    --card-base: #474747;
    --card-glow: #6a6a6a;
    --card-edge: #3b3b3b;
    --emblem-tone: #404040;
    --emblem-light: #565656;
    --ink-black: #0d0d0d;
    --ink-white: #f4f4f4;
    --emboss-light: rgba(255, 255, 255, 0.55);
    --emboss-dark: rgba(0, 0, 0, 0.75);
  }
  html, body {
    margin: 0;
    padding: 0;
    width: 1200px;
    height: 720px;
    overflow: hidden;
    background: var(--card-base);
  }
  .card {
    position: relative;
    width: 1200px;
    height: 720px;
    overflow: hidden;
    background:
      radial-gradient(ellipse 420px 220px at 420px 300px, var(--card-glow) 0%, rgba(106,106,106,0) 100%),
      radial-gradient(ellipse 900px 600px at 50% 50%, var(--card-base) 40%, var(--card-edge) 100%);
  }
  .emblem {
    position: absolute;
    border-radius: 40px;
    background: linear-gradient(160deg, var(--emblem-light), var(--emblem-tone));
  }
  .emblem--branch {
    left: 85px;
    top: 130px;
    width: 350px;
    height: 500px;
    border-radius: 60px 60px 200px 60px;
  }
  .emblem--dove {
    left: 285px;
    top: 155px;
    width: 145px;
    height: 170px;
    border-radius: 50%;
  }
  .brand {
    position: absolute;
    right: 100px;
    top: 222px;
    text-align: right;
  }
  .brand__name {
    margin: 0;
    font-family: "Tinos", "Times New Roman", serif;
    font-weight: 700;
    font-size: 75px;
    line-height: 1;
    letter-spacing: 1px;
    color: var(--ink-black);
    text-shadow: -2px -2px 0 var(--emboss-light), 3px 3px 3px var(--emboss-dark);
  }
  .brand__tagline {
    margin: 10px -6px 0 0;
    font-family: "Open Sans", Arial, sans-serif;
    font-size: 37px;
    line-height: 1;
    color: var(--ink-black);
    text-shadow: -1px -1px 0 var(--emboss-light), 2px 2px 2px var(--emboss-dark);
  }
  .divider {
    position: absolute;
    left: 587px;
    top: 392px;
    width: 531px;
    height: 4px;
    background: var(--ink-black);
    box-shadow: 0 -2px 0 var(--emboss-light), 0 3px 3px var(--emboss-dark);
  }
  .contact {
    position: absolute;
    right: 87px;
    top: 458px;
    margin: 0;
    font-family: "Open Sans", Arial, sans-serif;
    font-style: normal;
    font-size: 31px;
    line-height: 48px;
    text-align: right;
    color: var(--ink-white);
    text-shadow: 1px 2px 2px var(--emboss-dark);
  }
  .contact__line { display: block; }
</style>
</head>
<body>
  <div class="card">
    <div class="emblem emblem--branch" role="img" aria-label="Embossed olive branch, symbol of eternal peace"></div>
    <div class="emblem emblem--dove" role="img" aria-label="Small embossed dove in flight"></div>

    <div class="brand">
      <h1 class="brand__name">Quillstone</h1>
      <p class="brand__tagline">funeral services</p>
    </div>

    <div class="divider"></div>

    <address class="contact">
      <span class="contact__line">+639174826351</span>
      <span class="contact__line">darvik4521@pelmora.com</span>
      <span class="contact__line">corner of Brisco Avenue and Velhurst Street</span>
      <span class="contact__line">Makati City, Philippines</span>
    </address>
  </div>
</body>
</html>
```